cryotherapy business . Whole Body Cryotherapy, Localised Cryotherapy, Cryofacials

Need home page plus services, about, pricing, online booking, contact and blog page

I want something slick, hip and professional. Our studio colours are duck egg blue, white and grey

I would also like a social media scroll at the bottom of every page

I will upload some web designs that I like the look of

Target Market(s)

Men and Women 25-45

Industry/Entity Type

Health And Wellness

Coding

Coded - Design and coding required

Number of Pages Required

5+ page

Font styles to use
Serif
Sans Serif

Requirements
Must have
• Must be eye catching and easy to navigate
Nice to have
• animation
Should not have
• Not sure what the site should not have. I am fairly open to ideas as this is a brand new business.

```html
<!DOCTYPE html>
<html lang="en">
<head>
<meta charset="utf-8">
<title>Frostcare Studio</title>
<link rel="stylesheet" href="https://fonts.googleapis.com/css2?family=Oswald:wght@500;700&family=Raleway:ital,wght@0,300;0,400;0,500;0,600;0,700;1,400;1,500&display=swap">
<style>
:root{
  --duck:#a7cacc;
  --duck-dark:#8db7ba;
  --mist:#eef3f3;
  --navy:#2b3571;
  --ink:#1c1c1c;
  --grey:#555;
  --white:#fff;
}
*{box-sizing:border-box;margin:0;padding:0}
html,body{width:1200px;height:4818px;overflow:hidden}
body{font-family:"Raleway",sans-serif;color:var(--ink);background:var(--white);position:relative}
section,header,footer{position:absolute;left:0;width:1200px;overflow:hidden}
.abs{position:absolute}
.center{left:0;width:1200px;text-align:center}
.rule{position:absolute;left:565px;width:70px;height:4px;background:var(--ink)}
.rule.light{background:var(--white)}

/* hero */
.hero{top:0;height:677px;background:linear-gradient(180deg,#9fb2c4 0%,#c3cfdb 45%,#b2c0cf 100%)}
.hero-photo{position:absolute;inset:0;background:radial-gradient(ellipse at 52% 40%,#d9dfe6 0%,rgba(190,202,214,.6) 40%,rgba(150,168,186,.3) 75%)}
.brand-box{position:absolute;left:77px;top:0;width:208px;height:137px;background:var(--white);border-bottom:5px solid var(--duck);text-align:center;padding-top:38px;box-shadow:0 3px 8px rgba(0,0,0,.12)}
.brand-name{font-family:"Raleway",sans-serif;font-weight:600;font-size:22px;line-height:30px;color:#333;letter-spacing:.5px}
.nav{position:absolute;top:0;left:385px;height:62px;display:flex;align-items:center;gap:29px;font-size:14px;font-weight:500;color:var(--white);letter-spacing:.3px}
.nav .current{color:var(--navy);font-weight:600}
.booking-btn{position:absolute;left:931px;top:0;width:192px;height:62px;background:var(--navy);color:var(--white);font-size:15px;font-weight:600;display:flex;align-items:center;justify-content:center}
.hero-title{top:360px;font-family:"Oswald",sans-serif;font-weight:700;font-size:124px;color:var(--white);letter-spacing:2px;line-height:1}
.hero-sub{top:496px;font-size:26px;font-weight:600;color:var(--navy)}
.play{position:absolute;left:568px;top:554px}

/* welcome */
.welcome{top:677px;height:468px}
.mist-circle{position:absolute;border-radius:50%;background:var(--mist)}
.watermark{font-family:"Oswald",sans-serif;font-weight:700;font-size:118px;letter-spacing:10px;color:#e3eaea;line-height:1}
.welcome .watermark{top:20px;color:#dfe7e7}
.eyebrow{font-size:21px;font-weight:400}
.section-title{font-size:40px;font-weight:700;letter-spacing:.5px}
.lede{font-size:16px;font-style:italic;line-height:27px;color:#333}

/* services */
.services{top:1145px;height:677px;background:var(--duck);color:var(--white)}
.services .section-title{color:var(--white)}
.service-card{position:absolute;top:225px;width:328px;text-align:center}
.service-card .ph{height:219px}
.service-card h3{margin-top:36px;font-size:17px;font-weight:600;letter-spacing:.3px}
.service-card p{margin-top:18px;font-size:13px;line-height:27px;padding:0 22px}

/* benefits */
.benefits{top:1822px;height:708px}
.benefit{position:absolute;width:250px}
.benefit h4{font-size:16px;font-weight:700}
.benefit p{font-size:13px;color:#444;margin-top:7px}
.benefit.left{text-align:right}

/* testimonial */
.testimonial{top:2530px;height:397px;background:var(--duck);color:var(--white)}
.testimonial .section-title{color:var(--white)}

/* blog strip */
.blog-strip{top:2936px;height:250px}
.tile{position:absolute;top:0;width:292px;height:250px}
.blog-tag{position:absolute;left:32px;top:54px;background:var(--duck);color:#1f3350;font-size:14px;font-weight:600;padding:6px 14px;border-radius:3px}
.blog-text{position:absolute;left:32px;top:112px;width:240px;color:var(--white);font-size:16px;line-height:26px}

/* pricing */
.pricing{top:3186px;height:681px}
.price-row{position:absolute;left:233px;width:742px;height:105px;border-bottom:1px solid #e4e4e4}
.price-row h5{position:absolute;left:0;top:0;font-size:16px;font-weight:600}
.price-row .meta{position:absolute;left:0;top:30px;font-size:12px;color:#555}
.price-row .meta a{color:var(--duck-dark);font-style:italic;text-decoration:underline;margin-left:10px}
.price-row .amt{position:absolute;right:140px;top:-8px;font-size:30px;font-weight:600;text-align:right;line-height:1}
.price-row .was{position:absolute;right:140px;top:26px;font-size:13px;color:#555}
.select{position:absolute;right:2px;top:-8px;width:102px;height:42px;border:2px solid var(--duck);border-radius:4px;font-size:15px;font-weight:600;display:flex;align-items:center;justify-content:center}

/* cta */
.cta{top:3867px;height:365px}
.cta-half{position:absolute;top:0;width:600px;height:365px;text-align:center;color:var(--white)}
.cta-half h2{position:absolute;top:122px;width:600px;font-size:32px;font-weight:600}
.cta-half .sub{position:absolute;top:170px;width:600px;font-size:15px}
.cta-btn{position:absolute;left:211px;top:215px;width:190px;height:46px;border:2px solid var(--white);border-radius:4px;font-size:17px;font-weight:500;display:flex;align-items:center;justify-content:center}

/* contact footer */
.contact{top:4232px;height:519px}
.contact-item{position:absolute;left:503px;display:flex;align-items:center;gap:18px}
.contact-item .txt{font-size:13px;line-height:27px;color:#333}
.copyright{top:4751px;height:67px;background:var(--duck);color:var(--white)}
.copyright p{position:absolute;left:78px;top:25px;font-size:12px}
</style>
</head>
<body>

<header class="hero">
  <div class="hero-photo" role="img" aria-label="Woman seen from behind surrounded by cold cryotherapy mist"></div>
  <div class="brand-box"><div class="brand-name">FROSTCARE<br>STUDIO</div></div>
  <nav class="nav">
    <span class="current">HOME ▾</span><span>SERVICES</span><span>ABOUT</span><span>PRICING</span><span>BLOG</span><span>CONTACT</span>
  </nav>
  <div class="booking-btn">ONLINE BOOKING</div>
  <h1 class="abs center hero-title">STAY STRONG</h1>
  <p class="abs center hero-sub">REDUX BROUGHT ME BACK</p>
  <svg class="play" width="64" height="64" viewBox="0 0 64 64"><circle cx="32" cy="32" r="32" fill="#8bb7bb"/><path d="M26 20 L44 32 L26 44Z" fill="#fff"/></svg>
</header>

<section class="welcome">
  <div class="mist-circle" style="left:162px;top:-200px;width:876px;height:876px"></div>
  <div class="abs center watermark">CRYOTHERAPY</div>
  <p class="abs center eyebrow" style="top:107px">WELCOME TO</p>
  <h2 class="abs center section-title" style="top:142px">CRYOTHERAPY BUSINESS</h2>
  <div class="rule" style="top:204px"></div>
  <p class="abs lede" style="left:300px;width:600px;top:240px;text-align:center">Lorem Ipsum is simply dummy text of the printing and typesetting industry. Lorem Ipsum has been the industry's standard dummy text ever since the when an unknown printer</p>
  <svg class="abs" style="left:578px;top:352px" width="44" height="20" viewBox="0 0 44 20"><path d="M2 2 L22 17 L42 2" fill="none" stroke="#c9d6d7" stroke-width="2"/></svg>
</section>

<section class="services">
  <h2 class="abs center section-title" style="top:72px">SERVICES WE PROVIDED</h2>
  <div class="rule light" style="top:130px"></div>
  <p class="abs center" style="top:164px;font-size:14px;color:#2f3f45">Lorem Ipsum is simply dummy text of the printing and typesetting industry. Lorem Ipsum has been the.</p>
  <div class="service-card" style="left:77px">
    <div class="ph" role="img" aria-label="Client smiling inside a whole body cryotherapy chamber" style="background:linear-gradient(135deg,#1b2f9a,#3a5fd0 55%,#8aa0e0)"></div>
    <h3>WHOLE BODY CRYOTHERAPY</h3>
    <p>Lorem Ipsum is simply dummy text of the printing and typesetting industry. Lorem Ipsum has been the.</p>
  </div>
  <div class="service-card" style="left:436px">
    <div class="ph" role="img" aria-label="Localised cryotherapy applied to a client's face" style="background:linear-gradient(135deg,#eef0f2,#d9c2b0 55%,#6f8fb5)"></div>
    <h3>LOCALISED CRYOTHERAPY</h3>
    <p>Lorem Ipsum is simply dummy text of the printing and typesetting industry. Lorem Ipsum has been the.</p>
  </div>
  <div class="service-card" style="left:795px">
    <div class="ph" role="img" aria-label="Client receiving a cryofacial treatment" style="background:linear-gradient(135deg,#2a4f80,#5c86b0 50%,#d7dde3)"></div>
    <h3>CRYOFACIALS</h3>
    <p>Lorem Ipsum is simply dummy text of the printing and typesetting industry. Lorem Ipsum has been the.</p>
  </div>
</section>

<section class="benefits">
  <h2 class="abs center section-title" style="top:60px">CRYOTHERAPY BENEFITS</h2>
  <div class="rule" style="top:122px"></div>
  <svg class="abs" style="left:0;top:0" width="1200" height="708" viewBox="0 0 1200 708">
    <circle cx="600" cy="413" r="238" fill="none" stroke="#eef1f1" stroke-width="3"/>
    <g fill="#fff" stroke="#e6ecec" stroke-width="4">
      <circle cx="397" cy="235" r="46"/><circle cx="333" cy="403" r="46"/><circle cx="387" cy="575" r="46"/>
      <circle cx="805" cy="235" r="46"/><circle cx="868" cy="403" r="46"/><circle cx="815" cy="575" r="46"/>
    </g>
    <g fill="#a7cacc">
      <circle cx="397" cy="235" r="38"/><circle cx="333" cy="403" r="38"/><circle cx="387" cy="575" r="38"/>
      <circle cx="805" cy="235" r="38"/><circle cx="868" cy="403" r="38"/><circle cx="815" cy="575" r="38"/>
    </g>
    <g fill="none" stroke="#fff" stroke-width="2" stroke-linecap="round">
      <path d="M378 244 h38 l-6-12 l-12-4 l-8-8 l-10 10z"/>
      <circle cx="333" cy="400" r="13"/><path d="M320 420 q13 -8 26 0"/>
      <path d="M387 557 q14 14 6 30 q-12 6 -18 -6 q-2 -12 12 -24z"/>
      <path d="M795 222 h20 v26 h-20z M800 232 h10"/>
      <circle cx="868" cy="400" r="15"/><path d="M862 400 h12 M868 394 v12"/>
      <circle cx="815" cy="568" r="11"/><path d="M798 594 q17 -18 34 0"/>
    </g>
  </svg>
  <div class="abs" role="img" aria-label="Woman breathing out a cloud of cold vapour against a bright blue background" style="left:391px;top:204px;width:418px;height:418px;border-radius:50%;background:radial-gradient(circle at 45% 65%,#ffffff 0%,#d8eef2 25%,#5fcde0 55%,#2fb9d3 100%)"></div>
  <div class="benefit left" style="left:80px;top:206px"><h4>INJURY RECOVERY</h4><p>Lorem Ipsum is simply dummy text</p></div>
  <div class="benefit left" style="left:14px;top:380px"><h4>ANTI- AGEING</h4><p>Ipsum is simply dummy text</p></div>
  <div class="benefit left" style="left:80px;top:556px"><h4>METABOLISM</h4><p>Lorem Ipsum is simply dummy text</p></div>
  <div class="benefit" style="left:869px;top:206px"><h4>CHRONIC PAIN</h4><p>Lorem Ipsum is simply dummy text</p></div>
  <div class="benefit" style="left:932px;top:380px"><h4>MENTAL HEALTH</h4><p>Lorem Ipsum is simply dumm</p></div>
  <div class="benefit" style="left:886px;top:556px"><h4>INFLAMMATION</h4><p>Lorem Ipsum is simply dummy text</p></div>
</section>

<section class="testimonial">
  <h2 class="abs center section-title" style="top:60px">WHAT OUR CLIENT SAY</h2>
  <svg class="abs" style="left:580px;top:148px" width="40" height="34" viewBox="0 0 40 34" fill="#fff"><path d="M2 20 q0-16 16-20 v6 q-8 3-8 10 h8 v16 h-16z M22 20 q0-16 16-20 v6 q-8 3-8 10 h8 v16 h-16z"/></svg>
  <p class="abs lede" style="left:300px;width:600px;top:206px;text-align:center;color:#2f3f45">Lorem Ipsum is simply dummy text of the printing and typesetting industry. Lorem Ipsum has been the industry's standard dummy text ever since the when an unknown printer</p>
  <svg class="abs" style="left:555px;top:314px" width="90" height="14" viewBox="0 0 90 14" fill="none" stroke="#fff" stroke-width="1.5">
    <circle cx="7" cy="7" r="5"/><circle cx="26" cy="7" r="5"/><circle cx="45" cy="7" r="5"/><circle cx="64" cy="7" r="5" fill="#fff"/><circle cx="83" cy="7" r="5"/>
  </svg>
</section>

<section class="blog-strip">
  <div class="tile" style="left:0;background:linear-gradient(135deg,#2b3a8c,#3f55b0)" role="img" aria-label="Tired man resting his head in his hand">
    <span class="blog-tag">BLOG</span>
    <p class="blog-text">Lorem Ipsum is simply the dummy text of the .</p>
  </div>
  <div class="tile" style="left:303px;background:linear-gradient(180deg,#9fb4c4,#556a7d 60%,#3a4650)" role="img" aria-label="Runner stretching on a wet city street"></div>
  <div class="tile" style="left:606px;background:linear-gradient(180deg,#2f3338,#5d646b 50%,#8b939a)" role="img" aria-label="Runner's legs splashing through rain on the road"></div>
  <div class="tile" style="left:908px;background:linear-gradient(180deg,#4b4f55,#2a2d31 60%,#1a1c1f)" role="img" aria-label="Athlete tying a running shoe"></div>
</section>

<section class="pricing">
  <h2 class="abs center section-title" style="top:60px">OUR PRICE</h2>
  <div class="rule" style="top:120px"></div>
  <div class="price-row" style="top:192px"><h5>Whole Body Cryptotherapy (session 1)</h5><p class="meta">15 mins <a>Show Detail</a></p><span class="amt">£60</span><span class="was">£95</span><span class="select">Select</span></div>
  <div class="price-row" style="top:298px"><h5>Whole Body Cryptotherapy (session 2)</h5><p class="meta">15 mins <a>Show Detail</a></p><span class="amt">£70</span><span class="was">£95</span><span class="select">Select</span></div>
  <div class="price-row" style="top:402px"><h5>Whole Body Cryptotherapy (session 3)</h5><p class="meta">15 mins <a>Show Detail</a></p><span class="amt">£80</span><span class="was">£95</span><span class="select">Select</span></div>
  <div class="price-row" style="top:501px"><h5>Whole Body Cryptotherapy (session 4)</h5><p class="meta">15 mins <a>Show Detail</a></p><span class="amt">£90</span><span class="was">£95</span><span class="select">Select</span></div>
  <svg class="abs" style="left:576px;top:600px" width="48" height="20" viewBox="0 0 48 20"><path d="M2 10 H42 M34 3 L44 10 L34 17" fill="none" stroke="#a7cacc" stroke-width="4"/></svg>
</section>

<section class="cta">
  <div class="cta-half" style="left:0;background:linear-gradient(160deg,#2b3571,#33408a 60%,#253064)" role="img" aria-label="Cryotherapy chamber interior in deep blue light">
    <h2>BOOK AN APPOINTMENT</h2>
    <p class="sub">+Begin your cryo journey</p>
    <div class="cta-btn">BOOK ONLINE</div>
  </div>
  <div class="cta-half" style="left:600px;background:var(--duck)">
    <h2>NEED TO KNOW MORE</h2>
    <p class="sub" style="color:#e9f2f2">Before you start your cryo journey ?</p>
    <div class="cta-btn">TALK TO US</div>
  </div>
</section>

<footer class="contact">
  <div class="mist-circle" style="left:162px;top:-150px;width:876px;height:876px"></div>
  <div class="abs center watermark" style="top:40px;color:#e2e9e9">CRYOTHERAPY</div>
  <p class="abs center" style="top:124px;font-size:32px;font-weight:600">CRYOTHERAPY</p>
  <p class="abs center" style="top:160px;font-size:32px;font-weight:300">BUSINESS</p>
  <div class="contact-item" style="top:218px">
    <svg width="56" height="56" viewBox="0 0 56 56"><circle cx="28" cy="28" r="28" fill="#a7cacc"/><path d="M20 17 l5 0 l3 7 l-3 3 q3 6 8 8 l3-3 l7 3 l0 5 q-2 3 -6 2 q-14 -4 -19 -19 q-1 -4 2 -6z" fill="#fff"/></svg>
    <div class="txt">Cal Us Today :<br>123 456 7890</div>
  </div>
  <div class="contact-item" style="top:304px">
    <svg width="56" height="56" viewBox="0 0 56 56"><circle cx="28" cy="28" r="28" fill="#a7cacc"/><path d="M28 14 a10 10 0 0 1 10 10 q0 8 -10 19 q-10 -11 -10 -19 a10 10 0 0 1 10 -10z" fill="#fff"/><circle cx="28" cy="24" r="4" fill="#a7cacc"/></svg>
    <div class="txt">101 - Lorem ipsum is<br>simple text of print and.</div>
  </div>
  <div class="contact-item" style="top:390px">
    <svg width="56" height="56" viewBox="0 0 56 56"><circle cx="28" cy="28" r="28" fill="#a7cacc"/><rect x="16" y="19" width="24" height="18" rx="2" fill="#fff"/><path d="M16 21 l12 9 l12 -9" fill="none" stroke="#a7cacc" stroke-width="2"/></svg>
    <div class="txt">Email Us :<br>info@frostcarestudio.com</div>
  </div>
</footer>

<footer class="copyright">
  <p>©CRYOTHERAPY BUSINESS - 2019 All Right reserved.</p>
  <svg class="abs" style="left:944px;top:13px" width="180" height="42" viewBox="0 0 180 42" fill="none" stroke="#fff" stroke-width="1.5">
    <circle cx="21" cy="21" r="19"/><circle cx="67" cy="21" r="19"/><circle cx="113" cy="21" r="19"/><circle cx="159" cy="21" r="19"/>
  </svg>
</footer>

</body>
</html>
```